Design a clean homepage for a travel portal based in the US catering to Asians. The design should be able to be used on other pages, or color scheme menu layout, header and footer should be usable on other pages.

Include the main options for users to click, as an example some could be; 1. Local Tour Company 2. Local Tour Guide 3. Transportation Company 4. Tour Packages

Think like www.brushmarket-example.com who brings designers and clients together we are bringing Tour company, Tour guide, Bus/Transportation company directly to those who need it. This is for a two way portal, not a common one way portal like regular booking sites.

Assume that a person arrives or is planning on arriving at a destination, what are some options that should be on the page, layout of the options: squares, rectangles, stars, scroll slides, whatever makes you feel fun, elegant, fresh, uplifting.

Feelings we want to convey: fun, elegant, fresh, uplifting, interesting, energetic

Update:
When we said this should be a simple design, we meant simple for the end user to understand what was going on. I have attached a screenshot of a website, that it is very easy to understand what its purpose is.

How you decide to set up picture/scenery areas, logo area, menu area, where the options go is all up to you. Would like it to be clean and inviting, we would also like the options to be colors that call the users to action(make them click). This doesn't have to be colors so much as design. If you have further questions feel free to message me.

Attached is our logo in various styles for you to choose from.

Target Market(s)

Travel, package tours, international students, business trips

Industry/Entity Type

Travel Industry

Number of Pages Required

1 page

Colors
ec1f27
ffffff
0255a3
474747
7f7f7f
5c5c5c
aaaaaa

Requirements
Must have
• 1. Local Tour Company 2. Local Tour Guide 3. Transportation Company 4. Tour Packages
Should not have
• Our main goal is not to sell flights or hotel rooms, so this can be an element on the page(or not) but it should not be very central/obvious.

```html
<!DOCTYPE html>
<html lang="en">
<head>
<meta charset="utf-8">
<title>Skylark Travel – Home</title>
<link href="https://fonts.googleapis.com/css2?family=Roboto:wght@400;500;700&family=Roboto+Condensed:wght@300;400;700&display=swap" rel="stylesheet">
<style>
  :root {
    --navy: #2d3e4e;
    --teal: #245c7c;
    --teal-text: #1f5f80;
    --green: #7dc13a;
    --ink: #474747;
    --grey: #7f7f7f;
    --light: #aaaaaa;
    --panel: #f3f3f3;
    --white: #ffffff;
  }
  * { box-sizing: border-box; margin: 0; padding: 0; }
  html, body { width: 1200px; height: 1200px; overflow: hidden; background: var(--white); }
  body { position: relative; font-family: "Roboto", sans-serif; color: var(--ink); }
  .abs { position: absolute; }

  /* top bar */
  .topbar { left: 0; top: 0; width: 1200px; height: 32px; background: var(--navy); }
  .topbar a { position: absolute; top: 11px; font-size: 9px; font-weight: 700; color: var(--white); text-decoration: none; letter-spacing: .2px; white-space: nowrap; }
  .topbar a.active { color: #6fa9cf; }
  .social { position: absolute; top: 9px; width: 15px; height: 15px; background: #4d5e6e; }
  .social.on { background: var(--green); }

  /* header */
  .header { left: 0; top: 32px; width: 1200px; height: 96px; background: var(--white); }
  .tour { position: absolute; top: 32px; }
  .tour h3 { font-size: 14px; font-weight: 500; color: var(--teal-text); white-space: nowrap; }
  .tour p { font-size: 8.5px; color: var(--light); margin-top: 4px; white-space: nowrap; }
  .divider { position: absolute; top: 16px; width: 1px; height: 56px; background: #ececec; }
  .logo-cap { left: 590px; top: 8px; width: 100px; height: 100px; border-radius: 50%; background: var(--white); }
  .logo-dot { left: 629px; top: 26px; width: 22px; height: 22px; border-radius: 50%; background: #5aa9c9; }
  .logo { left: 560px; top: 62px; width: 160px; text-align: center; font-weight: 700; font-size: 24px; color: var(--teal-text); }
  .down { left: 624px; top: 108px; width: 32px; height: 32px; border-radius: 50%; background: var(--white); }

  /* hero */
  .hero { left: 0; top: 128px; width: 1200px; height: 576px;
    background: linear-gradient(180deg, #2fbfe6 0%, #8fdcf2 45%, #e9f6f8 62%, #f7f6f2 100%); }
  .hero-line { left: 640px; top: 290px; width: 1px; height: 95px; background: #6aaed0; }
  .hero-intro { left: 362px; top: 305px; width: 260px; text-align: right; font-size: 11.2px; line-height: 16.8px; color: #1c3f56; white-space: nowrap; }
  .hero-intro b { color: var(--green); font-weight: 700; }
  .hero-title { left: 656px; top: 300px; font-family: "Roboto Condensed", sans-serif; font-size: 31px; color: var(--teal-text); white-space: nowrap; }
  .hero-title b { font-weight: 700; }
  .hero-title span { font-weight: 300; font-size: 24px; }
  .hero-sub { left: 661px; top: 339px; font-size: 11.2px; color: #1c3f56; white-space: nowrap; }
  .pill { left: 489px; top: 385px; width: 304px; height: 64px; border-radius: 32px; background: var(--teal); }
  .pill .explore { position: absolute; left: 24px; top: 19px; font-family: "Roboto Condensed", sans-serif; font-size: 20px; font-weight: 300; color: #cfe7f2; }
  .pill .explore small { font-size: 10px; font-weight: 700; color: var(--white); }
  .pill .glass { position: absolute; left: 130px; top: 14px; width: 36px; height: 36px; border-radius: 50%; background: #e8f3f7; }
  .pill .tag { position: absolute; left: 182px; top: 19px; font-size: 10px; line-height: 13px; color: var(--white); white-space: nowrap; }
  .pill .tag i { font-style: normal; color: #8fd3ee; }
  .learn { left: 588px; top: 479px; width: 104px; height: 37px; border-radius: 19px; background: rgba(255,255,255,.6); }
  .learn span { position: absolute; left: 4px; top: 4px; width: 96px; height: 29px; border-radius: 15px; background: var(--green); color: var(--white); font-size: 9px; font-weight: 700; text-align: center; line-height: 29px; }
  .plane-badge { left: 616px; top: 680px; width: 48px; height: 48px; border-radius: 50%; background: var(--green); }

  /* offers */
  .offer-line { left: 640px; top: 728px; width: 0; height: 104px; border-left: 1px dotted #cfcfcf; }
  .offer-end { left: 637px; top: 830px; width: 6px; height: 6px; border-radius: 50%; border: 1px solid #cfcfcf; background: var(--white); }
  .offer h2 { font-family: "Roboto Condensed", sans-serif; font-weight: 400; font-size: 19px; color: #333; white-space: nowrap; }
  .offer h2 em { font-style: normal; color: var(--green); }
  .offer p { font-size: 11px; color: var(--grey); margin-top: 8px; white-space: nowrap; }
  .offer.left { right: 594px; top: 746px; text-align: right; }
  .offer.right { left: 674px; top: 746px; }
  .btn { position: absolute; top: 808px; width: 89px; height: 25px; border: 1px solid #d2d2d2; border-radius: 13px; font-size: 8.5px; color: var(--grey); text-align: center; line-height: 23px; background: var(--white); }

  /* services */
  .services { left: 0; top: 880px; width: 1200px; height: 320px; background: var(--panel); }
  .services h2 { position: absolute; left: 0; top: 62px; width: 1200px; text-align: center; font-family: "Roboto Condensed", sans-serif; font-weight: 700; font-size: 25px; color: #333; }
  .services h2 em { font-style: normal; font-weight: 400; color: var(--green); }
  .services .lead { position: absolute; left: 0; top: 103px; width: 1200px; text-align: center; font-size: 10px; line-height: 15.5px; color: var(--grey); }
  .service { position: absolute; top: 171px; width: 228px; height: 160px; }
  .service .photo { position: absolute; inset: 0; }
  .service .label { position: absolute; left: 14px; right: 14px; top: 92px; height: 32px; border-radius: 16px; background: var(--green); color: var(--white); font-size: 11px; font-weight: 700; text-align: center; line-height: 32px; letter-spacing: .3px; white-space: nowrap; }
</style>
</head>
<body>

<nav class="abs topbar">
  <a class="active" style="left:162px">HOME</a>
  <a style="left:232px">TOURS</a>
  <a style="left:311px">GUIDES</a>
  <a style="left:388px">ABOUT US</a>
  <a style="left:479px">CONTACT US</a>
  <a style="left:738px">➜ LOGIN / REGISTER</a>
  <a style="left:870px">$ DOLLAR</a>
  <a style="left:957px">● ENGLISH</a>
  <span class="social" style="left:1050px"></span>
  <span class="social on" style="left:1068px"></span>
  <span class="social" style="left:1086px"></span>
  <span class="social" style="left:1104px"></span>
</nav>

<header class="abs header">
  <div class="tour" style="left:162px"><h3>Asian tour</h3><p>More than 1.020 routes</p></div>
  <span class="divider" style="left:278px"></span>
  <div class="tour" style="left:292px"><h3>Africa tour</h3><p>More than 1.140 routes</p></div>
  <span class="divider" style="left:409px"></span>
  <div class="tour" style="left:424px"><h3>Europe tour</h3><p>More than 2.080 routes</p></div>
  <span class="divider" style="left:544px"></span>
  <span class="divider" style="left:735px"></span>
  <div class="tour" style="left:752px"><h3>Oceania tour</h3><p>More than 975 routes</p></div>
  <span class="divider" style="left:866px"></span>
  <div class="tour" style="left:884px"><h3>Other tour</h3><p>More than 140 routes</p></div>
  <span class="divider" style="left:1001px"></span>
  <div class="tour" style="left:1023px"><h3>Search tour</h3><p>Find your dream here</p></div>
</header>

<div class="abs logo-cap"></div>
<div class="abs logo-dot"></div>
<div class="abs logo">Skylark</div>

<section class="abs hero" role="img" aria-label="Beach illustration: traveller on a deck chair under a palm tree, airliner, seagulls, hot air balloons and starfish on white sand"></section>
<div class="abs down">
  <svg width="32" height="32" viewBox="0 0 32 32"><path d="M12 14l4 4 4-4" fill="none" stroke="#2f7fa6" stroke-width="2"/></svg>
</div>

<span class="abs hero-line"></span>
<svg class="abs" style="left:636px;top:286px" width="8" height="8"><circle cx="4" cy="4" r="3" fill="none" stroke="#6aaed0"/></svg>
<p class="abs hero-intro"><b>FIND MORE</b> About our sailing destination,<br>Matinas &amp; suggested itineraries, And make your<br>dream happen here.</p>
<h1 class="abs hero-title"><b>TRAVELING</b> <span>ALWAYS “GOOD IDEA”</span></h1>
<p class="abs hero-sub">It leaves you speecless, Then turns you into a Storyteller.</p>

<div class="abs pill">
  <span class="explore">Explore <small>here</small></span>
  <span class="glass" role="img" aria-label="Coconut drink illustration"></span>
  <span class="tag"><i>your passion</i> is to<br>exploring the world</span>
</div>
<div class="abs learn"><span>LEARN MORE</span></div>

<div class="abs plane-badge">
  <svg width="48" height="48" viewBox="0 0 48 48"><path d="M24 12c1.2 0 1.8 1.4 1.8 3v6l9 5v2.4l-9-2.6v5.4l3 2.2v2l-4.8-1.4-4.8 1.4v-2l3-2.2v-5.4l-9 2.6V26l9-5v-6c0-1.6.6-3 1.8-3z" fill="none" stroke="#fff" stroke-width="1.6" stroke-linejoin="round"/></svg>
</div>

<span class="abs offer-line"></span>
<span class="abs offer-end"></span>
<div class="abs offer left">
  <h2>Come to the <em>Tropial Paradise</em> 2015</h2>
  <p>Club royal resort Thailand, 7 night accommodation, just for $2.754 per adult</p>
</div>
<div class="abs offer right">
  <h2><em>Special</em> Offer Honeymoon Destinations</h2>
  <p>From $375 per passenger, Bali, Srilangka, Mauritius, make your dream happen..</p>
</div>
<span class="btn" style="left:418px">CHECK NOW</span>
<span class="btn" style="left:518px">BOOKING NOW</span>
<span class="btn" style="left:672px">CHECK NOW</span>
<span class="btn" style="left:772px">BOOKING NOW</span>

<section class="abs services">
  <h2>Travelers Choice of <em>Services</em></h2>
  <p class="lead">Lorem ipsum dolor sit amet, consectetuer adipiscing elit, sed diam nonummy nibh euismod tincidunt<br>ut laoreet dolore magna aliquam erat volutpat diam nonummy nibh.</p>
  <a class="service" style="left:160px">
    <div class="photo" role="img" aria-label="Photo of a local tour company office" style="background:linear-gradient(180deg,#4f8fd6 0%,#c9dcf2 55%,#3a4f8a 100%)"></div>
    <span class="label">LOCAL TOUR COMPANY</span>
  </a>
  <a class="service" style="left:404px">
    <div class="photo" role="img" aria-label="Photo of a local guide leading travellers" style="background:linear-gradient(180deg,#5a93d8 0%,#bcd3ef 55%,#34508c 100%)"></div>
    <span class="label">LOCAL TOUR GUIDE</span>
  </a>
  <a class="service" style="left:648px">
    <div class="photo" role="img" aria-label="Photo of a tour bus on a city street" style="background:linear-gradient(180deg,#8fa6c4 0%,#3b4256 60%,#2a2f3d 100%)"></div>
    <span class="label">TRANSPORTATION COMPANY</span>
  </a>
  <a class="service" style="left:892px">
    <div class="photo" role="img" aria-label="Photo of a city skyline for tour packages" style="background:linear-gradient(180deg,#5d86d0 0%,#2a4f9a 55%,#1b2e5c 100%)"></div>
    <span class="label">TOUR PACKAGES</span>
  </a>
</section>

</body>
</html>
```